An image to show that our fees are offset by our good management

We work in the property sector.
We'd like a slide showing that our fees weigh very little compared with the savings we can generate if we do our job properly as property managers.
To do this, we've come up with a slide with a scale showing our fees on the left (which weigh less or the same) than the items on the right.
On the right you can see:
Savings on building maintenance costs
Savings on running costs
Optimization of vacant periods
Good monitoring of disputes to avoid rental losses
We welcome any other ideas you may have to highlight this concept (even off-balance sheet).

```html
<!DOCTYPE html>
<html lang="en">
<head>
<meta charset="utf-8">
<title>Our fees are offset by good management</title>
<link href="https://fonts.googleapis.com/css2?family=Mulish:wght@800&display=swap" rel="stylesheet">
<style>
  :root {
    --bg: #ffffff;
    --ink: #555555;
    --beam: #111111;
    --fulcrum-dark: #625e5d;
    --fulcrum-light: #8f8f8f;
    --fees-blue: #45b0d8;
    --badge-yellow: #e8b420;
    --maintenance-pink: #e8357f;
    --running-orange: #f7ae45;
    --vacancy-purple: #b574aa;
    --disputes-green: #60e0b5;
    --icon: #ffffff;
  }
  * { box-sizing: border-box; margin: 0; padding: 0; }
  html, body { width: 1200px; height: 1200px; overflow: hidden; background: var(--bg); }
  .slide { position: relative; width: 1200px; height: 1200px; font-family: "Mulish", sans-serif; color: var(--ink); }
  .balance { position: absolute; inset: 0; }
  .fees-label {
    position: absolute; left: 216px; top: 501px; width: 140px;
    text-align: center; font-weight: 800; font-size: 16px;
  }
  .benefit {
    position: absolute; bottom: 552px; width: 78px;
    display: flex; flex-direction: column; align-items: center;
  }
  .benefit-label {
    font-weight: 800; font-size: 12px; line-height: 14px;
    text-align: center; margin-bottom: 10px; width: 110px;
  }
  .benefit-bar { width: 100%; display: flex; justify-content: center; align-items: flex-end; padding-bottom: 6px; }
  .benefit-bar svg { display: block; }
  .benefit--maintenance { left: 679px; }
  .benefit--maintenance .benefit-bar { height: 110px; background: var(--maintenance-pink); }
  .benefit--running { left: 772px; }
  .benefit--running .benefit-bar { height: 174px; background: var(--running-orange); }
  .benefit--vacancy { left: 866px; }
  .benefit--vacancy .benefit-bar { height: 138px; background: var(--vacancy-purple); }
  .benefit--disputes { left: 959px; }
  .benefit--disputes .benefit-bar { height: 110px; background: var(--disputes-green); padding-bottom: 12px; }
</style>
</head>
<body>
<main class="slide">
  <svg class="balance" width="1200" height="1200" viewBox="0 0 1200 1200" aria-hidden="true">
    <!-- fulcrum -->
    <polygon points="612,659 491,788 612,788" fill="var(--fulcrum-dark)"/>
    <polygon points="612,659 736,788 612,788" fill="var(--fulcrum-light)"/>
    <!-- beam -->
    <rect x="175" y="648" width="875" height="10" fill="var(--beam)"/>
    <!-- fees coin -->
    <circle cx="286" cy="587" r="59" fill="var(--fees-blue)"/>
    <circle cx="286" cy="587" r="33" fill="none" stroke="var(--icon)" stroke-width="4"/>
    <text x="286" y="600" text-anchor="middle" font-family="Mulish, sans-serif" font-weight="800" font-size="36" fill="var(--icon)">$</text>
    <!-- comparison badge -->
    <circle cx="612" cy="629" r="18" fill="var(--badge-yellow)"/>
    <text x="612" y="637" text-anchor="middle" font-family="Mulish, sans-serif" font-weight="800" font-size="22" fill="var(--icon)">≤</text>
  </svg>

  <p class="fees-label">Our Fess</p>

  <section class="benefit benefit--maintenance">
    <p class="benefit-label">Savings<br>on building<br>maintenance<br>costs</p>
    <div class="benefit-bar">
      <svg width="60" height="96" viewBox="0 0 60 96" fill="none" stroke="var(--icon)" stroke-width="4" stroke-linecap="round">
        <text x="30" y="22" text-anchor="middle" font-family="Mulish, sans-serif" font-weight="800" font-size="20" fill="var(--icon)" stroke="none">$</text>
        <line x1="10" y1="34" x2="48" y2="72"/>
        <line x1="8" y1="32" x2="14" y2="38" stroke-width="7"/>
        <line x1="44" y1="36" x2="20" y2="60"/>
        <path d="M44 36 a6 6 0 1 1 6 -8"/>
        <path d="M16 90 c-8 -4 -6 -14 0 -20 c0 6 4 6 4 2 c4 4 6 14 -4 18z" fill="var(--icon)" stroke="none"/>
      </svg>
    </div>
  </section>

  <section class="benefit benefit--running">
    <p class="benefit-label">Savings<br>on running<br>costs</p>
    <div class="benefit-bar">
      <svg width="64" height="90" viewBox="0 0 64 90">
        <text x="32" y="22" text-anchor="middle" font-family="Mulish, sans-serif" font-weight="800" font-size="20" fill="var(--icon)">$</text>
        <g transform="translate(32,60)" fill="var(--icon)">
          <rect x="-5" y="-28" width="10" height="56" rx="2"/>
          <rect x="-5" y="-28" width="10" height="56" rx="2" transform="rotate(45)"/>
          <rect x="-5" y="-28" width="10" height="56" rx="2" transform="rotate(90)"/>
          <rect x="-5" y="-28" width="10" height="56" rx="2" transform="rotate(135)"/>
          <circle r="21"/>
          <circle r="9" fill="var(--running-orange)"/>
        </g>
      </svg>
    </div>
  </section>

  <section class="benefit benefit--vacancy">
    <p class="benefit-label">Optimization<br>of vacant<br>periods</p>
    <div class="benefit-bar">
      <svg width="64" height="66" viewBox="0 0 64 66" fill="none" stroke="var(--icon)" stroke-width="2.5" stroke-linejoin="round">
        <rect x="22" y="2" width="20" height="16"/>
        <line x1="26" y1="8" x2="38" y2="8"/>
        <line x1="26" y1="12" x2="38" y2="12"/>
        <line x1="32" y1="18" x2="32" y2="34"/>
        <path d="M14 34 H50 L60 54 H4 Z"/>
        <rect x="4" y="54" width="56" height="8"/>
        <path d="M8 58 H56" stroke-dasharray="1.5 2"/>
      </svg>
    </div>
  </section>

  <section class="benefit benefit--disputes">
    <p class="benefit-label">Good<br>monitoring<br>of disputes<br>to avoid<br>rental losses</p>
    <div class="benefit-bar">
      <svg width="56" height="56" viewBox="0 0 56 56" fill="none" stroke="var(--icon)" stroke-width="3.5" stroke-linecap="round">
        <circle cx="24" cy="24" r="19"/>
        <line x1="38" y1="38" x2="52" y2="52" stroke-width="7"/>
        <path d="M12 24 q12 -12 24 0 q-12 12 -24 0z" stroke-width="2.5"/>
        <circle cx="24" cy="24" r="4" fill="var(--icon)" stroke="none"/>
      </svg>
    </div>
  </section>
</main>
</body>
</html>
```